Business Card Design Project

We need a simple business card design that uses our current logo.
We need to have the current logo put into a high res format.
We need to have 1 card made with contact information.
We will supply the information for the 4 employees.
Industry/Entity Type
Business
Requirements
Must have
- The contact information is as follows:
Mark Dellweather
Producer/CEO
c. 949-555-0147
f. 650-555-0193
markd@lanternbay.example
Al Vostrand, CFO
c. 949-555-0162
f. 650-555-0193
alv@lanternbay.example
Peter Malvane, PR
c. 267-555-0128
f. 650-555-0193
pmalvane@lanternbay.example
Tim Garrowby, Producer
c. 949-555-0184
f. 650-555-0193
timg@lanternbay.example
The address for all cards is:
318 W Calle Norvento #2715, San Clemente, CA 92681

```html
<!DOCTYPE html>
<html lang="en">
<head>
<meta charset="utf-8">
<title>Lantern Bay Media Business Card</title>
<link rel="stylesheet" href="https://fonts.googleapis.com/css2?family=Play:wght@400;700&display=swap">
<style>
  :root {
    --backdrop: #cfcfcf;
    --backdrop-deep: #a9a9a9;
    --card-black: #0b0c0e;
    --card-charcoal: #1d2024;
    --accent-blue: #4aa8ec;
    --accent-blue-light: #7cc6ff;
    --text-white: #f2f4f6;
  }
  * { box-sizing: border-box; margin: 0; padding: 0; }
  html, body { width: 1200px; height: 861px; overflow: hidden; }
  body {
    background: radial-gradient(ellipse at 50% 40%, var(--backdrop) 0%, var(--backdrop-deep) 100%);
    font-family: "Play", sans-serif;
    position: relative;
  }
  .card {
    position: absolute;
    top: 288px;
    width: 500px;
    height: 286px;
    background:
      linear-gradient(115deg, transparent 30%, rgba(255,255,255,0.06) 38%, transparent 46%),
      radial-gradient(ellipse at 50% 40%, var(--card-charcoal) 0%, var(--card-black) 75%);
    box-shadow: 0 14px 30px rgba(0,0,0,0.35);
    overflow: hidden;
    color: var(--text-white);
    text-align: center;
  }
  .card--front { left: 70px; }
  .card--back { left: 630px; }
  .card__frame { position: absolute; inset: 0; width: 100%; height: 100%; }
  .card__content { position: relative; height: 100%; display: flex; flex-direction: column; align-items: center; justify-content: center; }
  .brand-name {
    font-weight: 700;
    color: var(--accent-blue);
    letter-spacing: 1px;
    text-transform: uppercase;
  }
  .card--front .brand-name { font-size: 40px; }
  .web-address { margin-top: 14px; font-size: 21px; font-weight: 700; }
  .card--back .brand-name { font-size: 30px; margin-bottom: 12px; }
  .person-name { font-size: 25px; font-weight: 700; color: var(--accent-blue-light); letter-spacing: 1px; text-transform: uppercase; }
  .person-title { font-size: 14px; font-weight: 700; margin-bottom: 10px; }
  .contact-list { list-style: none; font-size: 12.5px; line-height: 1.6; }
  .contact-label { color: var(--accent-blue); font-weight: 700; margin-right: 3px; }
</style>
</head>
<body>
  <section class="card card--front">
    <svg class="card__frame" viewBox="0 0 500 286" aria-hidden="true">
      <rect x="0" y="140" width="8" height="146" fill="var(--accent-blue)"/>
      <rect x="492" y="0" width="8" height="146" fill="var(--accent-blue)"/>
      <polyline points="0,232 26,232 50,256 50,286" fill="none" stroke="var(--accent-blue)" stroke-width="6"/>
      <polyline points="500,54 474,54 450,30 450,0" fill="none" stroke="var(--accent-blue)" stroke-width="6"/>
    </svg>
    <div class="card__content">
      <p class="brand-name">Lantern Bay Media</p>
      <p class="web-address">www.lanternbay.example</p>
    </div>
  </section>

  <section class="card card--back">
    <svg class="card__frame" viewBox="0 0 500 286" aria-hidden="true">
      <rect x="0" y="140" width="8" height="146" fill="var(--accent-blue)"/>
      <rect x="492" y="0" width="8" height="146" fill="var(--accent-blue)"/>
      <polyline points="0,232 26,232 50,256 50,286" fill="none" stroke="var(--accent-blue)" stroke-width="6"/>
      <polyline points="500,54 474,54 450,30 450,0" fill="none" stroke="var(--accent-blue)" stroke-width="6"/>
    </svg>
    <div class="card__content">
      <p class="brand-name">Lantern Bay Media</p>
      <p class="person-name">Mark Dellweather</p>
      <p class="person-title">Producer/CEO</p>
      <ul class="contact-list">
        <li><span class="contact-label">A.</span>318 W Calle Norvento #2715, San Clemente, CA 92681</li>
        <li><span class="contact-label">C.</span>949-555-0147</li>
        <li><span class="contact-label">F.</span>650-555-0193</li>
        <li><span class="contact-label">E.</span>markd@lanternbay.example</li>
      </ul>
    </div>
  </section>
</body>
</html>
```